MTSS Pyramid graphic needed for use in presentations and on my website

I am a consultant and need graphics to represent the MTSS pyramid (educational terminology) for use on my website and in slide decks. I've included documentation below that shows the MTSS pyramid, some preferences I have thought of, and my color palette. The MTSS pyramid is well-known in my field and I'd like one that I can use in all my presentations and on my website that looks professional and modern.

Target Market(s)

Educational leaders and educators

Industry/Entity Type

Educational Consulting

Font styles to use
Serif
Sans Serif

Colors
00AB8E
00BBA5
67D7C9
C6EFE9
E9F9F6
6B429C
8869AF
B7A5CE
E3DAEB
F3F0F8

Requirements
Must have
• a pyramid that can be recognized as an MTSS pyramid, use of colors that align with my color palette, a professional, modern look and feel, 3 sections with the largest at the bottom of the pyramid
Nice to have
• rounded corners, maybe 3D
Should not have
• a pyramid in a different shape or orientation, any more or fewer than 3 sections

```html
<!DOCTYPE html>
<html lang="en">
<head>
<meta charset="UTF-8">
<title>MTSS Pyramid</title>
<link rel="stylesheet" href="https://fonts.googleapis.com/css2?family=Arimo:wght@700&family=Nunito:wght@900&display=swap">
<style>
  :root {
    --bg: #ffffff;
    --teal-dark: #00AB8E;
    --teal: #00BBA5;
    --teal-light: #67D7C9;
    --teal-pale: #C6EFE9;
    --purple-dark: #6B429C;
    --purple: #8869AF;
    --purple-light: #B7A5CE;
    --purple-pale: #E3DAEB;
    --label-white: #ffffff;
  }
  * { margin: 0; padding: 0; box-sizing: border-box; }
  html, body {
    width: 1200px;
    height: 750px;
    overflow: hidden;
    background: var(--bg);
  }
  .canvas {
    position: relative;
    width: 1200px;
    height: 750px;
    font-family: "Nunito", "Arial Rounded MT Bold", sans-serif;
  }
  .pyramid { position: absolute; inset: 0; }
  .face { stroke-linejoin: round; stroke-width: 10; }
  .gloss { stroke: none; }
  .edge { fill: none; stroke-linejoin: round; stroke-linecap: round; stroke-width: 2.5; stroke: rgba(255,255,255,0.45); }
  .tier-label {
    font-family: "Arimo", Arial, sans-serif;
    font-weight: 700;
    font-size: 23px;
    fill: var(--label-white);
    stroke: #7d8a8c;
    stroke-width: 1px;
    paint-order: stroke;
  }
  .callout {
    position: absolute;
    right: 223px;
    text-align: right;
    font-weight: 900;
    font-size: 27px;
    line-height: 34px;
    letter-spacing: 0.8px;
  }
  .callout .word { display: block; }
  .callout .rule { display: block; height: 2px; margin: 0 0 0 auto; }
  .callout-tier3 { top: 129px; color: var(--purple); }
  .callout-tier3 .rule { width: 458px; background: var(--purple); }
  .callout-tier2 { top: 292px; color: var(--teal); }
  .callout-tier2 .rule { width: 348px; background: var(--teal); }
  .callout-tier1 { top: 453px; color: var(--teal-dark); }
  .callout-tier1 .rule { width: 229px; background: var(--teal-dark); }
</style>
</head>
<body>
<div class="canvas">
  <svg class="pyramid" width="1200" height="750" viewBox="0 0 1200 750" aria-label="Three-tier MTSS pyramid">
    <defs>
      <linearGradient id="t1-left" x1="0" y1="0" x2="1" y2="1">
        <stop offset="0" stop-color="#1fbfa3"/><stop offset="1" stop-color="#009e84"/>
      </linearGradient>
      <linearGradient id="t1-right" x1="0" y1="0" x2="1" y2="1">
        <stop offset="0" stop-color="#22c9b4"/><stop offset="1" stop-color="#00b09a"/>
      </linearGradient>
      <linearGradient id="t2-left" x1="0" y1="0" x2="1" y2="1">
        <stop offset="0" stop-color="#5ed2c3"/><stop offset="1" stop-color="#2bbfae"/>
      </linearGradient>
      <linearGradient id="t2-right" x1="0" y1="0" x2="1" y2="1">
        <stop offset="0" stop-color="#7fe0d4"/><stop offset="1" stop-color="#48cbbb"/>
      </linearGradient>
      <linearGradient id="t3-left" x1="0" y1="0" x2="1" y2="1">
        <stop offset="0" stop-color="#8a67b8"/><stop offset="1" stop-color="#6B429C"/>
      </linearGradient>
      <linearGradient id="t3-right" x1="0" y1="0" x2="1" y2="1">
        <stop offset="0" stop-color="#a88bcb"/><stop offset="1" stop-color="#8869AF"/>
      </linearGradient>
      <linearGradient id="sheen" x1="0" y1="0" x2="0" y2="1">
        <stop offset="0" stop-color="#ffffff" stop-opacity="0.28"/>
        <stop offset="0.55" stop-color="#ffffff" stop-opacity="0.06"/>
        <stop offset="1" stop-color="#ffffff" stop-opacity="0"/>
      </linearGradient>
      <filter id="soft-shadow" x="-10%" y="-10%" width="120%" height="130%">
        <feDropShadow dx="0" dy="3" stdDeviation="3" flood-color="#1d3b38" flood-opacity="0.3"/>
      </filter>
      <filter id="label-depth" x="-20%" y="-40%" width="140%" height="180%">
        <feDropShadow dx="1" dy="2" stdDeviation="0.8" flood-color="#3a4446" flood-opacity="0.7"/>
      </filter>
    </defs>

    <g class="tier1">
      <polygon class="face" fill="url(#t1-left)" stroke="url(#t1-left)" points="189,439 445,500 454,664 97,567"/>
      <polygon class="face" fill="url(#t1-right)" stroke="url(#t1-right)" points="445,500 655,426 751,549 454,664"/>
      <polygon class="gloss" fill="url(#sheen)" points="189,439 445,500 655,426 751,549 454,664 97,567"/>
      <polyline class="edge" points="97,567 189,439 445,500 655,426 751,549"/>
      <line class="edge" x1="445" y1="500" x2="454" y2="664"/>
      <text class="tier-label" filter="url(#label-depth)" x="592" y="558" transform="rotate(-17 592 558)" text-anchor="middle">Tier 1</text>
    </g>

    <g class="tier2" filter="url(#soft-shadow)">
      <polygon class="face" fill="url(#t2-left)" stroke="url(#t2-left)" points="311,250 438,284 446,488 194,418"/>
      <polygon class="face" fill="url(#t2-right)" stroke="url(#t2-right)" points="438,284 533,248 655,410 446,488"/>
      <polygon class="face" fill="#8ee5da" stroke="#8ee5da" stroke-width="6" points="311,250 430,244 533,248 438,284"/>
      <polygon class="gloss" fill="url(#sheen)" points="311,250 438,284 533,248 655,410 446,488 194,418"/>
      <polyline class="edge" points="194,418 311,250 438,284 533,248 655,410"/>
      <line class="edge" x1="438" y1="284" x2="446" y2="488"/>
      <text class="tier-label" filter="url(#label-depth)" x="522" y="358" transform="rotate(-17 522 358)" text-anchor="middle">Tier 2</text>
    </g>

    <g class="tier3" filter="url(#soft-shadow)">
      <polygon class="face" fill="url(#t3-left)" stroke="url(#t3-left)" points="425,96 433,263 322,234"/>
      <polygon class="face" fill="url(#t3-right)" stroke="url(#t3-right)" points="425,96 528,228 433,263"/>
      <polygon class="gloss" fill="url(#sheen)" points="425,96 528,228 433,263 322,234"/>
      <polyline class="edge" points="322,234 425,96 528,228"/>
      <line class="edge" x1="425" y1="96" x2="433" y2="263"/>
      <text class="tier-label" filter="url(#label-depth)" x="477" y="227" transform="rotate(-17 477 227)" text-anchor="middle">Tier 3</text>
    </g>
  </svg>

  <div class="callout callout-tier3">
    <span class="word">Intensive</span>
    <span class="rule"></span>
    <span class="word">Intervention</span>
  </div>
  <div class="callout callout-tier2">
    <span class="word">Target</span>
    <span class="rule"></span>
    <span class="word">Intervention</span>
  </div>
  <div class="callout callout-tier1">
    <span class="word">Core</span>
    <span class="rule"></span>
    <span class="word">Instruction</span>
  </div>
</div>
</body>
</html>
```